A3 Event Poster for School Fundraiser

We are looking for a bold, engaging, and professional A3 poster design to promote a special school fundraising event. A top athlete will be visiting a primary school to inspire children, encourage participation in sport, and help launch a fundraising initiative to raise money for new PE/sports equipment for the school.

The poster will be displayed prominently outside the school and shared with parents and families. Its purpose is to generate excitement, explain the event quickly, and encourage parents/families to sponsor and get involved.

We work with about 50 different athletes so will need the design to be easy to alter the picture of the athlete/name etc so it can be replicated across the different athletes.

Target Market(s)

Priamary School Parents/Communities

Industry/Entity Type

Education

Font styles to use
Other font styles liked:
• The logo font is Rajdhani. ‘Corvel’ is bold, ‘Pennix’ is semibold and the strapline is regular.

Requirements
Must have
• Space for the Event Date (that school can write in themselves), A picture of the visiting athlete and their bio (with ability to easily change)
Nice to have
• Bold, eye-catching

```html
<!DOCTYPE html>
<html lang="en">
<head>
<meta charset="utf-8">
<title>Corvel Pennix – School Fundraiser Poster</title>
<link rel="stylesheet" href="https://fonts.googleapis.com/css2?family=Rajdhani:wght@400;600;700&family=Barlow+Condensed:wght@700;800&family=Poppins:wght@400;600;700&display=swap">
<style>
  :root{
    --purple:#662a7b;
    --lime:#c4fd6f;
    --lime-text:#b6f74f;
    --red:#e31e3a;
    --ink:#1d1d1f;
    --white:#ffffff;
  }
  *{box-sizing:border-box;margin:0;padding:0}
  html,body{width:927px;height:1200px;overflow:hidden;background:var(--white)}
  .poster{position:relative;width:927px;height:1200px;overflow:hidden;background:var(--white);font-family:"Poppins",sans-serif;color:var(--ink)}
  .shapes{position:absolute;inset:0}
  .brand{position:absolute;left:63px;top:72px;display:flex;align-items:center;gap:14px}
  .brand-dot{width:62px;height:62px;border-radius:50%;background:var(--red)}
  .brand-name{font-family:"Rajdhani",sans-serif;font-weight:700;font-size:84px;line-height:1;color:var(--purple);letter-spacing:1px}
  .strapline{position:absolute;left:142px;top:148px;font-family:"Rajdhani",sans-serif;font-weight:400;font-size:25px;color:var(--purple)}
  .headline{position:absolute;left:62px;top:390px;font-family:"Barlow Condensed",sans-serif;font-weight:700;font-size:54px;line-height:49px;color:var(--white);text-transform:uppercase}
  .appeal{position:absolute;left:62px;top:565px;font-weight:600;font-size:35px;line-height:45px;color:var(--lime-text)}
  .benefits{position:absolute;left:61px;top:673px;list-style:none}
  .benefits li{display:flex;align-items:center;gap:12px;height:33px;font-size:18px;color:var(--white)}
  .benefits svg{width:19px;height:19px}
  .mission{position:absolute;left:27px;top:800px;font-family:"Barlow Condensed",sans-serif;font-weight:800;font-size:30px;line-height:29px;letter-spacing:-1.2px;color:var(--white);text-transform:uppercase}
  .info-row{position:absolute;left:61px;display:flex;align-items:center;gap:13px}
  .info-icon{width:63px;height:63px;border-radius:50%;background:var(--red);display:flex;align-items:center;justify-content:center}
  .info-text{font-size:18px;line-height:22px;color:var(--ink)}
  .info-text strong{font-weight:700}
  .date{top:951px}
  .venue{top:1032px}
  .phone{position:absolute;left:61px;top:1119px;font-weight:700;font-size:29px;color:var(--red);letter-spacing:-1px}
  .athlete-role{position:absolute;left:507px;top:962px;font-weight:600;font-size:28px;color:var(--lime-text)}
  .athlete-bio{position:absolute;left:507px;top:1016px;width:400px;font-size:20.5px;line-height:21.6px;color:var(--white);white-space:nowrap}
</style>
</head>
<body>
<div class="poster">
  <svg class="shapes" width="927" height="1200" viewBox="0 0 927 1200">
    <defs>
      <linearGradient id="visit-tones" x1="0" y1="0" x2="1" y2="1">
        <stop offset="0" stop-color="#d9c3a6"/>
        <stop offset="0.5" stop-color="#e6b9a0"/>
        <stop offset="1" stop-color="#b85a4c"/>
      </linearGradient>
      <linearGradient id="portrait-tones" x1="0" y1="0" x2="0" y2="1">
        <stop offset="0" stop-color="#3a62b0"/>
        <stop offset="0.6" stop-color="#5a4038"/>
        <stop offset="1" stop-color="#2b3f86"/>
      </linearGradient>
    </defs>
    <polygon points="414,0 795,0 600,520 315,300" fill="var(--lime)"/>
    <path role="img" aria-label="Photo of the visiting athlete smiling beside a pupil" fill="url(#visit-tones)"
      d="M700,144 L927,144 L927,700 Q905,729 865,729 L520,729 Q492,729 502,700 L598,225 Q618,144 700,144 Z"/>
    <path fill="var(--purple)"
      d="M170,302 L575,302 Q630,305 618,370 L462,840 Q440,905 360,920 L0,920 L0,505 L48,395 Q80,302 170,302 Z"/>
    <path fill="var(--purple)"
      d="M396,1200 L468,962 Q490,890 585,882 L927,882 L927,1200 Z"/>
    <circle cx="720" cy="795" r="157" fill="var(--lime)"/>
    <circle role="img" aria-label="Portrait of the Olympic volleyball player" cx="720" cy="795" r="136" fill="url(#portrait-tones)"/>
  </svg>

  <div class="brand">
    <div class="brand-dot"></div>
    <div class="brand-name">Corvel Pennix</div>
  </div>
  <div class="strapline">Moving young minds</div>

  <h1 class="headline">Inspirational<br>athlete visiting our<br>school</h1>
  <p class="appeal">Help us raise funds for<br>new sports equipment</p>

  <ul class="benefits">
    <li><svg viewBox="0 0 20 20"><circle cx="10" cy="10" r="10" fill="#fff"/><path d="M5.5 10.3l3 3 6-6.3" stroke="#662a7b" stroke-width="2.4" fill="none" stroke-linecap="round" stroke-linejoin="round"/></svg>Be inspired</li>
    <li><svg viewBox="0 0 20 20"><circle cx="10" cy="10" r="10" fill="#fff"/><path d="M5.5 10.3l3 3 6-6.3" stroke="#662a7b" stroke-width="2.4" fill="none" stroke-linecap="round" stroke-linejoin="round"/></svg>Make a difference</li>
    <li><svg viewBox="0 0 20 20"><circle cx="10" cy="10" r="10" fill="#fff"/><path d="M5.5 10.3l3 3 6-6.3" stroke="#662a7b" stroke-width="2.4" fill="none" stroke-linecap="round" stroke-linejoin="round"/></svg>Get Active</li>
  </ul>

  <p class="mission">Inspiring every child to lead an<br>active, resilient and healthy life</p>

  <div class="info-row date">
    <div class="info-icon">
      <svg width="34" height="34" viewBox="0 0 34 34" fill="none" stroke="#fff" stroke-width="2.6" stroke-linecap="round">
        <rect x="3" y="6" width="24" height="22" rx="3"/>
        <line x1="3" y1="13" x2="27" y2="13"/>
        <line x1="9" y1="3" x2="9" y2="8"/><line x1="15" y1="3" x2="15" y2="8"/><line x1="21" y1="3" x2="21" y2="8"/>
        <circle cx="25" cy="25" r="6.5" fill="#e31e3a"/>
        <path d="M25 22v3.3l2 1.5"/>
      </svg>
    </div>
    <div class="info-text"><strong>16 October, 2026</strong><br>11 AM - 06 PM</div>
  </div>

  <div class="info-row venue">
    <div class="info-icon">
      <svg width="26" height="32" viewBox="0 0 26 32">
        <path d="M13 1C6.4 1 1.5 6 1.5 12.3 1.5 20 13 31 13 31s11.5-11 11.5-18.7C24.5 6 19.6 1 13 1z" fill="#fff"/>
        <circle cx="13" cy="12.5" r="4.5" fill="#e31e3a"/>
      </svg>
    </div>
    <div class="info-text">123 Anywhere St.,<br>Any City, ST 12345</div>
  </div>

  <div class="phone">+123-456-7890</div>

  <h2 class="athlete-role">Olympic Volleyball Player</h2>
  <p class="athlete-bio">Marcus is a dynamic English<br>volleyball player and coach,<br>known for his leadership on and off<br>the court and his passion for<br>inspiring the next generation<br>through sport.</p>
</div>
</body>
</html>
```